Flyer for the Harvest Lantern Gathering 2018

Design a flyer for our annual conference with basic information about the conference: conference logo and year,

Location:
Dunmore Community Center (Downtown Portland)
482 Willowby Street, Portland, ME 04117,

Date:
August 24th, 25th and 26th, 2018
Start time 6:00PM

I would like the following three words added to the flyer. These words describe the vision of the conference:
Prophetic, Worship, Prayer

```html
<!DOCTYPE html>
<html lang="en">
<head>
<meta charset="UTF-8">
<title>Harvest Lantern Gathering 2018 — Flyer</title>
<link rel="stylesheet" href="https://fonts.googleapis.com/css2?family=Archivo+Black&family=Montserrat:wght@500;600;700;800&display=swap">
<style>
  :root {
    --orange: #f07a22;
    --orange-light: #f6a21e;
    --ink: #2b2b2b;
    --grey: #6f6f6f;
    --rule: #d9d9d9;
    --paper: #ffffff;
    --backdrop: #ece9e4;
  }
  * { box-sizing: border-box; margin: 0; padding: 0; }
  html, body { width: 1200px; height: 1200px; overflow: hidden; background: var(--backdrop); }
  .flyer {
    position: absolute; left: 190px; top: 20px;
    width: 820px; height: 1160px;
    background: var(--paper); overflow: hidden;
    font-family: "Montserrat", sans-serif; color: var(--ink);
    box-shadow: 0 6px 24px rgba(0,0,0,.18);
  }
  .hero-photo {
    position: absolute; left: 0; top: 0; width: 820px; height: 660px;
    background: linear-gradient(160deg, #f4f3ef 0%, #e6e4de 45%, #8d8a86 75%, #3d4a66 100%);
  }
  .brand {
    position: absolute; left: 270px; top: 70px; width: 280px;
    display: flex; flex-direction: column; align-items: center; gap: 14px;
  }
  .brand-dot { width: 74px; height: 74px; border-radius: 50%; background: var(--orange-light); }
  .brand-name { font-weight: 700; font-size: 40px; letter-spacing: 3px; color: var(--ink); }
  .panel { position: absolute; left: 0; top: 0; width: 820px; height: 1160px; }
  .title {
    position: absolute; left: 0; width: 820px; top: 668px; text-align: center;
    font-family: "Archivo Black", sans-serif;
  }
  .title-main { font-size: 64px; color: var(--orange-light); line-height: 1; }
  .title-sub { font-size: 31px; color: var(--ink); margin-top: 12px; letter-spacing: .5px; line-height: 1.1; }
  .vision {
    position: absolute; top: 810px; left: 0; width: 820px;
    display: flex; justify-content: center; gap: 46px;
  }
  .vision-item { display: flex; align-items: center; gap: 12px; font-weight: 800; font-size: 24px; letter-spacing: 1px; }
  .icon-ring {
    width: 46px; height: 46px; border-radius: 50%; border: 3px solid var(--orange-light);
    display: flex; align-items: center; justify-content: center;
  }
  .details {
    position: absolute; left: 46px; top: 874px; width: 728px; height: 176px;
    border: 2px solid var(--rule); border-radius: 14px;
    display: flex; padding: 22px 24px; gap: 20px;
  }
  .details-col { display: flex; flex-direction: column; gap: 20px; justify-content: center; }
  .details-col.when { flex: 0 0 300px; }
  .details-col.where { flex: 1 1 auto; }
  .detail-row { display: flex; align-items: center; gap: 16px; font-weight: 600; font-size: 20px; line-height: 1.25; }
  .detail-icon {
    flex: none; width: 50px; height: 50px; border-radius: 50%;
    background: #7a7a7a; border: 4px solid #c9c9c9;
    display: flex; align-items: center; justify-content: center;
  }
  .accent { color: var(--orange); font-weight: 700; }
  .venue { font-weight: 800; color: var(--orange); font-size: 19px; white-space: nowrap; }
  .address { font-size: 18px; font-weight: 600; }
  .contact-band {
    position: absolute; left: 0; bottom: 0; width: 820px; height: 82px;
    background: var(--orange); color: #fff;
    display: flex; align-items: center; justify-content: center; gap: 44px;
    font-size: 18px; font-weight: 600;
  }
  .contact-item { display: flex; align-items: center; gap: 10px; }
</style>
</head>
<body>
<main class="flyer">
  <div class="hero-photo" role="img" aria-label="Photo of a speaker presenting to a seated audience in a bright white room"></div>

  <div class="brand">
    <div class="brand-dot"></div>
    <div class="brand-name">LANTERNCON</div>
  </div>

  <svg class="panel" viewBox="0 0 820 1160" aria-hidden="true">
    <polygon points="0,636 290,556 820,528 820,1160 0,1160" fill="#ffffff"/>
    <polyline points="0,636 290,556 820,528" fill="none" stroke="#f07a22" stroke-width="8"/>
  </svg>

  <header class="title">
    <h1 class="title-main">LANTERNCON 2018</h1>
    <h2 class="title-sub">HARVEST LANTERN GATHERING</h2>
  </header>

  <section class="vision">
    <div class="vision-item">
      <span class="icon-ring"><svg width="24" height="22" viewBox="0 0 24 22"><path d="M12 21 L2 11 A5.5 5.5 0 0 1 12 4 A5.5 5.5 0 0 1 22 11 Z" fill="#f6a21e"/></svg></span>
      PROPHETIC
    </div>
    <div class="vision-item">
      <span class="icon-ring"><svg width="22" height="24" viewBox="0 0 22 24"><path d="M8 3 L20 1 V17" fill="none" stroke="#f6a21e" stroke-width="3"/><circle cx="5" cy="19" r="4" fill="#f6a21e"/><circle cx="17" cy="17" r="4" fill="#f6a21e"/><line x1="8" y1="3" x2="8" y2="19" stroke="#f6a21e" stroke-width="3"/></svg></span>
      WORSHIP
    </div>
    <div class="vision-item">
      <span class="icon-ring"><svg width="24" height="24" viewBox="0 0 24 24"><polygon points="12,1 15,9 23,9 17,14 19,22 12,17 5,22 7,14 1,9 9,9" fill="#f6a21e"/></svg></span>
      PRAYER
    </div>
  </section>

  <section class="details">
    <div class="details-col when">
      <div class="detail-row">
        <span class="detail-icon"><svg width="24" height="24" viewBox="0 0 24 24"><rect x="2" y="4" width="20" height="18" rx="2" fill="none" stroke="#fff" stroke-width="2"/><line x1="2" y1="9" x2="22" y2="9" stroke="#fff" stroke-width="2"/><line x1="7" y1="1" x2="7" y2="6" stroke="#fff" stroke-width="2"/><line x1="17" y1="1" x2="17" y2="6" stroke="#fff" stroke-width="2"/></svg></span>
        <span>August 24th,<br>25th &amp; 26th, 2018</span>
      </div>
      <div class="detail-row">
        <span class="detail-icon"><svg width="24" height="24" viewBox="0 0 24 24"><circle cx="12" cy="12" r="10" fill="none" stroke="#fff" stroke-width="2"/><polyline points="12,6 12,12 16,14" fill="none" stroke="#fff" stroke-width="2"/></svg></span>
        <span>Start time <span class="accent">6:00PM</span></span>
      </div>
    </div>
    <div class="details-col where">
      <div class="detail-row">
        <span class="detail-icon"><svg width="22" height="26" viewBox="0 0 22 26"><path d="M11 25 C4 16 2 12 2 9 A9 9 0 0 1 20 9 C20 12 18 16 11 25 Z" fill="none" stroke="#fff" stroke-width="2"/><circle cx="11" cy="9" r="3" fill="#fff"/></svg></span>
        <span>
          <span class="venue">Dunmore Community Center</span><br>
          <span class="address">(Downtown Portland)<br>482 Willowby Street,<br>Portland, ME 04117,</span>
        </span>
      </div>
    </div>
  </section>

  <footer class="contact-band">
    <span class="contact-item"><svg width="18" height="18" viewBox="0 0 24 24"><path d="M6 2 L10 7 L8 10 C9 13 11 15 14 16 L17 14 L22 18 L19 22 C10 21 3 14 2 5 Z" fill="#fff"/></svg>(207) 555 0142</span>
    <span class="contact-item"><svg width="20" height="16" viewBox="0 0 20 16"><rect x="1" y="1" width="18" height="14" fill="none" stroke="#fff" stroke-width="2"/><polyline points="1,1 10,9 19,1" fill="none" stroke="#fff" stroke-width="2"/></svg>hello@lanternhall.org</span>
    <span class="contact-item"><svg width="18" height="18" viewBox="0 0 24 24"><circle cx="12" cy="12" r="10" fill="none" stroke="#fff" stroke-width="2"/><ellipse cx="12" cy="12" rx="4" ry="10" fill="none" stroke="#fff" stroke-width="2"/><line x1="2" y1="12" x2="22" y2="12" stroke="#fff" stroke-width="2"/></svg>www.lanterngather.org</span>
  </footer>
</main>
</body>
</html>
```